Mortgage firm needs clean and simple wordpress website and logo

The competition is for design only, and the winning design for the homepage will be expected to create a second design for a simpler template for additional pages.

We need a logo and basic wordpress website design for a Sydney based mortgage firm.
We need a clean and simple logo and website, based on the mortgage/accounting/finance/tax industry. Simple, credible and official colors.

The logo is expected to be so simple that we have combined into the one job.
If you submit a logo design and we choose it along with someone else's website design you will be paid a bonus of $60. The website design will still win the competition as per normal.

Current website is old and terrible but gives you an idea of the sitemap (super simple) and what they do: http://www.lendbridgeloans.com.au/

We will integrate a mortgage calculator into the site.
The calculator is adjustable in styles, you can see it here: http://www.lendbridgeloans.com.au/mortgagecalculator/

We want original different to copy-and-paste template looking designs.
We like simple websites with a long home page and a few additional pages like https://www.homefundpath.com.au/

We are based in Sydney Australia and are mortgage brokers

We want a clean, formal, credible site, limited pages.

The project is guaranteed, so go for it.

Example of basic template after home page complete: http://lendbridgeloans.com.au/template_example.jpg

Target Market(s)

Mortgage and banking clients

Industry/Entity Type

Finance

Number of Pages Required

1 page

Requirements
Must have
• A simple logo, Wordpress capable, be able to incorporate the mortgage calculator (on the home page if needed as well as its own page)
Nice to have
• VIdeo - something free but nice

```html
<!DOCTYPE html>
<html lang="en">
<head>
<meta charset="utf-8">
<title>Harbourline Lending – Home</title>
<link href="https://fonts.googleapis.com/css2?family=Exo+2:wght@500;600;700&family=Montserrat:wght@700;800&family=Open+Sans:wght@400;600;700&family=Lato:ital,wght@0,400;0,700;1,400&display=swap" rel="stylesheet">
<style>
:root{
  --blue:#0a78b4;
  --blue-dark:#07587f;
  --orange:#f0801f;
  --orange-dark:#d86a10;
  --ink:#222;
  --text:#555;
  --band:#f1f1f1;
  --line:#d9d9d9;
  --footer:#2b2b2b;
  --footer-dark:#1f1f1f;
  --social-a:#3b5a9a;
  --social-b:#1a84c4;
  --social-c:#d24a2e;
  --white:#fff;
}
*{box-sizing:border-box;margin:0;padding:0}
html,body{width:1200px;height:2560px;overflow:hidden}
body{position:relative;background:var(--white);font-family:"Open Sans",sans-serif;color:var(--text)}
.abs{position:absolute}

/* header */
.site-header{position:absolute;left:0;top:0;width:1200px;height:112px;background:linear-gradient(#fafafa,#e2e2e2)}
.top-contact{position:absolute;left:614px;top:0;width:422px;height:34px;background:var(--blue);display:flex;align-items:center;gap:24px;padding-left:20px;color:#fff;font-size:13.5px;font-weight:600;border-bottom:3px solid var(--orange);white-space:nowrap}
.top-contact span{display:flex;align-items:center;gap:8px}
.top-contact::after{content:"";position:absolute;right:-30px;top:0;border-top:34px solid var(--orange);border-right:30px solid transparent}
.top-contact::before{content:"";position:absolute;left:-24px;top:0;border-top:34px solid var(--blue);border-left:24px solid transparent}
.brand{position:absolute;left:160px;top:14px;display:flex;align-items:center;gap:12px}
.brand-mark{width:56px;height:56px;background:var(--blue);border-radius:4px}
.brand-name{font-family:"Exo 2",sans-serif;font-weight:700;font-size:34px;line-height:1;color:var(--blue)}
.main-nav{position:absolute;left:525px;top:66px;display:flex;font-size:16px;font-weight:600;color:#333}
.main-nav a{padding:0 22px;border-left:1px solid #bbb;color:inherit;text-decoration:none}
.main-nav a:first-child{border-left:none;color:var(--blue)}

/* hero */
.hero{position:absolute;left:0;top:112px;width:1200px;height:529px;background:linear-gradient(180deg,#8aa3b4 0%,#c9c2b4 45%,#4d5c3c 80%,#5d6d45 100%)}
.hero-band{position:absolute;left:0;top:355px;width:600px;height:110px;background:linear-gradient(90deg,rgba(0,0,0,.55),rgba(0,0,0,.25) 80%,rgba(0,0,0,0))}
.hero-tagline{position:absolute;left:133px;top:365px;font-family:"Montserrat",sans-serif;font-weight:800;font-size:31px;line-height:38px;color:#fff;text-transform:uppercase}
.hero-tagline .l2{padding-left:108px}
.hero-tagline em{font-style:normal;color:var(--orange)}
.quick-contact{position:absolute;left:740px;top:21px;width:332px;height:485px;background:var(--orange);border-radius:6px;box-shadow:0 4px 10px rgba(0,0,0,.35)}
.qc-title{position:absolute;left:-4px;top:17px;width:322px;height:46px;background:var(--blue);border-radius:4px;border:2px solid var(--blue-dark);color:#fff;font-family:"Exo 2",sans-serif;font-size:27px;font-weight:500;display:flex;align-items:center;padding-left:70px}
.qc-title svg{position:absolute;left:20px;top:6px}
.field{position:absolute;left:23px;width:283px;height:38px;background:#fff;border-radius:3px;font-size:12px;color:#333;padding:11px 12px}
.field.half{width:137px}
.qc-button{position:absolute;left:23px;top:439px;width:283px;height:45px;background:var(--blue);border-radius:3px;color:#fff;font-family:"Montserrat",sans-serif;font-weight:700;font-size:15px;display:flex;align-items:center;justify-content:center;border-bottom:3px solid var(--blue-dark)}

/* welcome */
.welcome-title{position:absolute;left:163px;top:650px;font-family:"Exo 2",sans-serif;font-weight:700;font-size:27px;color:var(--ink);line-height:34px}
.welcome-title strong{display:block;color:var(--blue)}
.welcome-rule{position:absolute;left:163px;top:728px;width:424px;height:2px;background:var(--line)}
.welcome-rule::before{content:"";position:absolute;left:0;top:0;width:150px;height:2px;background:var(--orange)}
.welcome-copy{position:absolute;left:163px;top:745px;width:424px;font-size:11.3px;line-height:19px;color:#555}
.welcome-copy p{margin-bottom:12px}
.watch-label{position:absolute;left:955px;top:700px;font-size:13px;color:#333}
.video{position:absolute;left:637px;top:750px;width:400px;height:220px;background:linear-gradient(135deg,#8a8f95,#c8c2bc 50%,#5d5d60)}
.video-bar{position:absolute;left:0;bottom:0;width:100%;height:16px;background:#222;display:flex;align-items:center;padding:0 8px;gap:8px;font-size:8px;color:#ccc}
.video-track{flex:1;height:3px;background:#666}
.video-play{position:absolute;left:180px;top:80px}

/* features */
.features{position:absolute;left:0;top:1040px;width:1200px;height:415px;background:var(--band);border-top:1px solid #e5e5e5}
.feature{position:absolute;top:48px;width:290px;text-align:center}
.feature-icon{width:112px;height:112px;border-radius:50%;margin:0 auto;display:flex;align-items:center;justify-content:center}
.feature h3{margin-top:24px;font-family:"Exo 2",sans-serif;font-weight:600;font-size:19px;color:var(--ink);letter-spacing:.5px}
.feature p{margin:12px auto 0;width:200px;font-size:13px;line-height:20px;color:#333}
.feature.wide p{width:245px}
.divider-v{position:absolute;top:40px;width:2px;height:330px;background:linear-gradient(#f1f1f1,#e0e0e0,#f1f1f1)}

/* section headings */
.section-title{position:absolute;left:0;width:1200px;text-align:center;font-family:"Exo 2",sans-serif;font-weight:600;font-size:28px;color:var(--blue)}
.section-title em{font-style:normal;color:var(--orange)}
.section-rule{position:absolute;left:368px;width:466px;height:2px;background:var(--line)}
.section-rule::before{content:"";position:absolute;left:148px;top:0;width:170px;height:2px;background:var(--orange)}

/* partners */
.partner{position:absolute;width:165px;height:62px;border:1px solid #e3e3e3;border-radius:3px;background:#fff;display:flex;align-items:center;justify-content:center}
.partner i{display:block;width:90px;height:24px;border-radius:3px;background:#d6dde3}

/* testimonials */
.testimonials{position:absolute;left:0;top:1903px;width:1200px;height:400px;background:var(--band)}
.testimonial{position:absolute;top:127px;width:437px;height:150px}
.avatar{position:absolute;left:0;top:0;width:97px;height:97px;border-radius:50%;border:3px solid var(--orange);background:linear-gradient(#d8c3b0,#9b7e6a)}
.quote{position:absolute;left:122px;top:4px;width:315px;font-family:"Lato",sans-serif;font-style:italic;font-size:11.6px;line-height:21px;color:#555}
.quote-mark{position:absolute;left:110px;top:-4px;font-family:Georgia,serif;font-size:40px;color:#ccc;line-height:1}
.quote-base{position:absolute;left:0;top:122px;width:437px;height:1px;background:#d3d3d3}
.author{position:absolute;left:203px;top:135px;font-size:12px;font-weight:700;color:var(--blue)}
.dots{position:absolute;left:1003px;top:2161px;display:flex;gap:5px}
.dots i{width:8px;height:8px;border-radius:50%;background:#c8c8c8}
.dots i:first-child{background:var(--blue)}

/* footer */
.footer-wave{position:absolute;left:0;top:2150px}
.footer{position:absolute;left:0;top:2260px;width:1200px;height:255px;background:linear-gradient(var(--footer),var(--footer-dark))}
.footer-col{position:absolute;top:52px;color:#ddd;font-size:11.5px}
.footer-col h4{font-size:14px;font-weight:700;color:#fff;padding-bottom:10px;border-bottom:1px solid #444;margin-bottom:14px;width:175px}
.footer-col ul{list-style:none}
.footer-col li{margin-bottom:16px;padding-left:14px;position:relative}
.footer-col li::before{content:"";position:absolute;left:0;top:7px;width:4px;height:4px;border-radius:50%;background:#ccc}
.footer-col li.current{color:var(--orange);font-weight:700}
.contact-line{display:flex;gap:9px;align-items:center;margin-bottom:10px}
.social{display:flex;align-items:center;gap:10px;margin-bottom:14px;line-height:13px}
.social i{width:30px;height:30px;border-radius:50%;display:block}
.social b{display:block;font-weight:600;color:#fff;font-size:11.5px}
.map{width:222px;height:120px;border:3px solid #ddd;background:linear-gradient(135deg,#c8d8e8,#e6e2d4 55%,#b9cfe2)}
.copyright{position:absolute;left:0;top:2515px;width:1200px;height:45px;background:var(--orange);color:#fff;font-size:11.5px;display:flex;align-items:center;justify-content:center}
</style>
</head>
<body>

<header class="site-header">
  <div class="top-contact">
    <span><svg width="14" height="14" viewBox="0 0 24 24"><path fill="#fff" d="M6.6 10.8a15 15 0 006.6 6.6l2.2-2.2c.3-.3.7-.4 1-.2 1.1.4 2.3.6 3.6.6.6 0 1 .4 1 1V20c0 .6-.4 1-1 1A17 17 0 013 4c0-.6.4-1 1-1h3.5c.6 0 1 .4 1 1 0 1.3.2 2.5.6 3.6.1.3 0 .7-.2 1z"/></svg>+612 9400 1234</span>
    <span><svg width="15" height="12" viewBox="0 0 24 18"><rect width="24" height="18" rx="2" fill="#fff"/><path d="M1 2l11 8 11-8" stroke="#0a78b4" stroke-width="2" fill="none"/></svg>inquiry@harbourlinelending.com</span>
  </div>
  <div class="brand"><span class="brand-mark"></span><span class="brand-name">Harbourline<br>Lending</span></div>
  <nav class="main-nav">
    <a href="#">Home</a><a href="#">About Us</a><a href="#">Mortgagecalculator</a><a href="#">Contact Us</a>
  </nav>
</header>

<section class="hero">
  <div class="abs" role="img" aria-label="Photo of a smiling family standing beside their car in front of a suburban home" style="inset:0"></div>
  <div class="hero-band"></div>
  <h1 class="hero-tagline">Your <em>Protection</em> is<br><span class="l2">Our <em>Commitment</em></span></h1>
  <form class="quick-contact">
    <div class="qc-title">
      <svg width="28" height="30" viewBox="0 0 28 30"><rect x="3" y="4" width="22" height="25" rx="2" fill="none" stroke="#fff" stroke-width="2"/><rect x="9" y="1" width="10" height="6" rx="1" fill="#fff"/><path d="M8 13h12M8 18h12M8 23h8" stroke="#fff" stroke-width="2"/></svg>
      Quick Contact
    </div>
    <div class="field" style="top:85px">Your Name:</div>
    <div class="field" style="top:135px">Zip Code:</div>
    <div class="field" style="top:184px">Date of Birth (MM/DD/YYYY):</div>
    <div class="field" style="top:230px">Phone:</div>
    <div class="field" style="top:277px">Email:</div>
    <div class="field" style="top:323px"></div>
    <div class="field half" style="top:369px"></div>
    <div class="field half" style="top:369px;left:169px"></div>
    <div class="qc-button">GO TO NEXT STEP</div>
  </form>
</section>

<section class="welcome">
  <h2 class="welcome-title">Welcome To<strong>Harbourline Lending</strong></h2>
  <div class="welcome-rule"></div>
  <div class="welcome-copy">
    <p>We have arranged finance for clients over many years through banks, non-bank lenders, mortgage managers and brokers.</p>
    <p>With a lending panel that includes the major banks through to more exclusive lenders, as well as private loan funding, there is a wide choice of finance options to suit your individual requirements.</p>
    <p>We believe it's not just long term employees that should be eligible for finance. Business owners, self-employed borrowers and contractors who are often unfairly dismissed when it comes to bank credit assessment, are welcome to apply with Harbourline Lending. In some cases a quickly funded short term private loan for a 6 months or 12 months term may be all that is needed as a temporary lending solution.</p>
  </div>
  <svg class="abs" style="left:895px;top:705px" width="60" height="42" viewBox="0 0 60 42"><path d="M56 8C36 4 16 12 6 38" stroke="#333" stroke-width="1.5" fill="none"/><path d="M2 30l4 9 7-7" stroke="#333" stroke-width="1.5" fill="none"/></svg>
  <div class="watch-label">Watch Video</div>
  <div class="video" role="img" aria-label="Video still of a mortgage adviser meeting a couple at a table">
    <svg class="video-play" width="40" height="40" viewBox="0 0 40 40"><circle cx="20" cy="20" r="19" fill="#c8461a" stroke="#f0801f" stroke-width="2"/><path d="M15 11l13 9-13 9z" fill="#fff"/></svg>
    <div class="video-bar"><span>▶</span><span class="video-track"></span><span>0:00/0:32</span></div>
  </div>
</section>

<section class="features">
  <div class="feature" style="left:118px">
    <div class="feature-icon" style="background:var(--orange)">
      <svg width="56" height="48" viewBox="0 0 56 48"><rect x="4" y="12" width="48" height="32" rx="4" fill="#fff"/><path d="M19 12V6h18v6" stroke="#fff" stroke-width="4" fill="none"/><rect x="24" y="24" width="8" height="7" fill="#f0801f"/><path d="M4 27h48" stroke="#f0801f" stroke-width="2"/></svg>
    </div>
    <h3>Experience</h3>
    <p>Harbourline Lending have been organising and managing money for clients for over 25 years using our access to banks, private lenders and brokers within Australia.</p>
  </div>
  <div class="divider-v" style="left:413px"></div>
  <div class="feature" style="left:428px">
    <div class="feature-icon" style="background:var(--blue)">
      <svg width="56" height="48" viewBox="0 0 56 48"><path d="M30 4L14 27h12l-4 18 20-26H30z" fill="#fff"/><path d="M4 16h10M2 24h8M6 32h8" stroke="#fff" stroke-width="3" stroke-linecap="round"/></svg>
    </div>
    <h3>Fast</h3>
    <p>We can provide money in 24 Hours, providing you meet the loan criteria. Unlike banks that might take months to complete a loan, we can react to your demands quickly.</p>
  </div>
  <div class="divider-v" style="left:723px"></div>
  <div class="feature wide" style="left:765px">
    <div class="feature-icon" style="background:var(--blue)">
      <svg width="56" height="56" viewBox="0 0 56 56"><rect x="10" y="24" width="30" height="24" rx="3" fill="#fff"/><path d="M16 24v-7a9 9 0 0118 0v7" stroke="#fff" stroke-width="4" fill="none"/><circle cx="40" cy="36" r="6" fill="none" stroke="#fff" stroke-width="3"/><path d="M44 40l8 8M48 44l3-3" stroke="#fff" stroke-width="3"/></svg>
    </div>
    <h3>Private</h3>
    <p>Our specialty is private lending for residential, commercial and industrial properties. We generally look for registered first mortgage security with up to 80% loan funding based on the property valuation, the type of security and the borrower profile.</p>
  </div>
</section>

<section class="partners">
  <h2 class="section-title" style="top:1500px">Our Mortgage Brokers <em>Make Home Loans Easy</em></h2>
  <div class="section-rule" style="top:1562px"></div>
  <div class="partner" style="left:163px;top:1612px"><i></i></div>
  <div class="partner" style="left:340px;top:1612px"><i></i></div>
  <div class="partner" style="left:518px;top:1612px"><i></i></div>
  <div class="partner" style="left:696px;top:1612px"><i></i></div>
  <div class="partner" style="left:875px;top:1612px"><i></i></div>
  <div class="partner" style="left:163px;top:1700px"><i></i></div>
  <div class="partner" style="left:340px;top:1700px"><i></i></div>
  <div class="partner" style="left:518px;top:1700px"><i></i></div>
  <div class="partner" style="left:696px;top:1700px"><i></i></div>
  <div class="partner" style="left:875px;top:1700px"><i></i></div>
  <div class="partner" style="left:163px;top:1788px"><i></i></div>
  <div class="partner" style="left:340px;top:1788px"><i></i></div>
  <div class="partner" style="left:518px;top:1788px"><i></i></div>
  <div class="partner" style="left:696px;top:1788px"><i></i></div>
  <div class="partner" style="left:875px;top:1788px"><i></i></div>
</section>

<section class="testimonials">
  <h2 class="section-title" style="top:35px">Clients <em>Testimonials</em></h2>
  <div class="section-rule" style="top:88px"></div>
  <div class="testimonial" style="left:163px">
    <div class="avatar" role="img" aria-label="Client portrait"></div>
    <span class="quote-mark">“</span>
    <p class="quote">Lorem ipsum dolor sit amet, consectet uer adipiscing elit, sed diam nonummy nibh euis mod tincidun nt ut laoreetml dolore magna aliquam erat volutpat. Ut wisi enim ad minim veniam, quis nostrud exer.</p>
    <div class="quote-base"></div>
    <div class="author">- Mr. Ravi Delmonte</div>
  </div>
  <div class="testimonial" style="left:625px">
    <div class="avatar" role="img" aria-label="Client portrait"></div>
    <span class="quote-mark">“</span>
    <p class="quote">Lorem ipsum dolor sit amet, consectet uer adipiscing elit, sed diam nonummy nibh euis mod tincidun nt ut laoreetml dolore magna aliquam erat volutpat. Ut wisi enim ad minim veniam, quis nostrud exer.</p>
    <div class="quote-base"></div>
    <div class="author">- Mr. Ravi Delmonte</div>
  </div>
</section>
<div class="dots"><i></i><i></i><i></i></div>

<svg class="footer-wave" width="1200" height="115" viewBox="0 0 1200 115">
  <path d="M0 40 C300 60 500 140 760 110 C980 85 1100 40 1200 0 V115 H0z" fill="#2b2b2b"/>
  <path d="M560 78 C800 95 1050 60 1200 8 V40 C1060 92 820 110 560 78z" fill="#f0801f"/>
</svg>

<footer class="footer">
  <div class="footer-col" style="left:163px">
    <h4 style="width:140px">Quick Links</h4>
    <ul>
      <li class="current">Home</li><li>About Us</li><li>Mortgagecalculator</li><li>Contact Us</li>
    </ul>
  </div>
  <div class="footer-col" style="left:357px">
    <h4>Contact Information</h4>
    <div style="font-weight:700;color:#fff;margin-bottom:2px">Harbourline Lending</div>
    <div style="margin-bottom:10px;line-height:15px">g04/115 Harbour Ln, Eastwood<br>NSW 2122</div>
    <div class="contact-line"><svg width="11" height="11" viewBox="0 0 24 24"><path fill="#f0801f" d="M6.6 10.8a15 15 0 006.6 6.6l2.2-2.2c.3-.3.7-.4 1-.2 1.1.4 2.3.6 3.6.6.6 0 1 .4 1 1V20c0 .6-.4 1-1 1A17 17 0 013 4c0-.6.4-1 1-1h3.5c.6 0 1 .4 1 1 0 1.3.2 2.5.6 3.6.1.3 0 .7-.2 1z"/></svg>+612 9400 1234</div>
    <div class="contact-line"><svg width="11" height="11" viewBox="0 0 24 24"><path fill="#f0801f" d="M6.6 10.8a15 15 0 006.6 6.6l2.2-2.2c.3-.3.7-.4 1-.2 1.1.4 2.3.6 3.6.6.6 0 1 .4 1 1V20c0 .6-.4 1-1 1A17 17 0 013 4c0-.6.4-1 1-1h3.5c.6 0 1 .4 1 1 0 1.3.2 2.5.6 3.6.1.3 0 .7-.2 1z"/></svg>+612 9400 1234</div>
    <div class="contact-line"><svg width="12" height="9" viewBox="0 0 24 18"><rect width="24" height="18" rx="2" fill="#f0801f"/><path d="M1 2l11 8 11-8" stroke="#2b2b2b" stroke-width="2" fill="none"/></svg>inquiry@harbourlinelending.com</div>
  </div>
  <div class="footer-col" style="left:612px">
    <h4 style="width:228px">Location Map</h4>
    <div class="map" role="img" aria-label="Street map showing the office location with a pin"></div>
  </div>
  <div class="footer-col" style="left:922px">
    <h4 style="width:112px">Follow Us</h4>
    <div class="social"><i style="background:var(--social-a)"></i><span><b>FACEPAGE</b>Become A Fan</span></div>
    <div class="social"><i style="background:var(--social-b)"></i><span><b>CHIRPER</b>Join Us On</span></div>
    <div class="social"><i style="background:var(--social-c)"></i><span><b>CIRCLES +</b>Join Us On</span></div>
  </div>
</footer>
<div class="copyright">Copyright © 2016 Harbourline Lending. All Rights Reserved.</div>

</body>
</html>
```